Velto-Primed Sports Cutting edge banner ad designs

Velto-primed sports is about to launch a new compresssion sportswear brand.

we are looking to team with a designer that can help us estabish a cutting edge look for our website. Our main products as we launch will be arm sleeves and headbands.

This first project will require
2 hero banners (1600 by 900) pixels. Submit to pixelharbor as 800x450 as they would accept the large format. I will request this upon acceptance
First Banner
should specify our slogan "Be RARE" or "B RARE", in a cutting edge, sporty font. please feel free to be creative with the slogan style and layout, you may even use our logo to represent the B.
include:
Free U.S. shipping on orders over $50
$3.99 shipping on everything else

Second Banner
Change the images
Change the slogan to BE WILD
Include:

Mix-n-match
5 for $50, & free shipping
(any sleeve or headband)

Once we finalize our designer, we will need additional design work for the remianing portions of the site. If you will not able to handle more work quickly within the next week, please do not enter this contest.

I have provided images from our photo shoot and logos to be used in the design. Please do not use other stock images, other than for minor composition or background effects. All the images I have provided are copyrighted, please dont use for any other purpose.

I have also attached the banner work from our previous designer for which we are not crazy about.

part of this design selection will be the editing of the images themselves. Also, when we shot the models some of the sleeves were too big, if you notice any sagging in the images please edit them so they look tighter.

Reason: I have only recieved a few design so far, so i am extending the period.

Reason: Need more designs

Target Market(s)

sports and athletic customers.

Colors
f37122

Requirements
Must have
• I want people to see this banner and think, wow this is cool they look edgy, professional, I want to find out more? be cutting edge, with a sports touch. spend some time editing the images and make the text like catching.
Nice to have
• I have attached a screen shot from an UGT clothing site. i really like how they display some product and the layout, but I would like to some how add an image or two from our models. Not all the sleeves ir headbands i have attached need to be used...
• Please use the Orange logo. Prefer to have a darker overall Lightroom type feel
Should not have
• dont make it too sexy and turn off potential moms from buying. we need to appeal to the women with the headbands, but also make moms comfortable going to our site with thier young boys and picking out arm eleves for them.

```html
<!DOCTYPE html>
<html lang="en">
<head>
<meta charset="utf-8">
<title>Velto-Primed Sports – Hero Banners</title>
<link rel="stylesheet" href="https://fonts.googleapis.com/css2?family=Anton&family=Oswald:wght@300;400;600;700&display=swap">
<style>
  :root {
    --page: #ffffff;
    --ink-dark: #0c0d10;
    --text-light: #f2f4f7;
    --frame-line: rgba(200, 205, 215, 0.45);
    --wild-blue: #1ea2ee;
    --wild-blue-deep: #0b5fb8;
    --wild-band: #0a4ea6;
    --rare-pink: #f0329a;
    --rare-pink-deep: #c41a72;
    --rare-band: #b21f4a;
    --stripe-grey: rgba(150, 155, 165, 0.28);
  }
  * { box-sizing: border-box; margin: 0; padding: 0; }
  html, body { width: 1000px; height: 1200px; overflow: hidden; background: var(--page); }
  .canvas { position: relative; width: 1000px; height: 1200px; }

  .banner { position: absolute; left: 0; width: 1000px; height: 563px; overflow: hidden; background: var(--ink-dark); }
  .banner--wild { top: 22px; }
  .banner--rare { top: 600px; }
  .banner__backdrop { position: absolute; inset: 0; }

  .photo { position: absolute; }
  .banner--wild .photo--models {
    left: 70px; top: 40px; width: 350px; height: 470px;
    background: linear-gradient(180deg, #c9d6e2 0%, #8aa5bf 45%, #2c3440 100%);
    border-radius: 40% 40% 8px 8px / 18% 18% 8px 8px;
    opacity: 0.85;
  }
  .banner--rare .photo--model {
    left: 40px; top: 20px; width: 380px; height: 543px;
    background: linear-gradient(170deg, #e7c88c 0%, #c99a66 40%, #8c5d48 65%, #2a2224 100%);
    border-radius: 48% 52% 0 0 / 30% 30% 0 0;
    opacity: 0.9;
  }

  .brand { position: absolute; right: 70px; top: 62px; display: flex; align-items: center; gap: 10px; }
  .brand__mark { width: 18px; height: 18px; }
  .banner--wild .brand__mark { background: var(--wild-blue); }
  .banner--rare .brand__mark { background: var(--rare-pink); }
  .brand__name {
    font-family: "Oswald", sans-serif; font-weight: 400; font-size: 30px;
    letter-spacing: 0.5px; color: #c9ccd2;
  }

  .slogan {
    position: absolute; right: 62px;
    font-family: "Anton", sans-serif; font-size: 168px; line-height: 1;
    letter-spacing: 2px; -webkit-background-clip: text; background-clip: text; color: transparent;
  }
  .banner--wild .slogan {
    top: 150px;
    background-image: linear-gradient(180deg, #7fd4ff 0%, var(--wild-blue) 45%, var(--wild-blue-deep) 100%);
  }
  .banner--rare .slogan {
    top: 170px;
    background-image: linear-gradient(180deg, #ff9ad2 0%, var(--rare-pink) 45%, var(--rare-pink-deep) 100%);
  }

  .offer { position: absolute; left: 500px; width: 445px; top: 333px; text-align: center; color: var(--text-light); font-family: "Oswald", sans-serif; text-transform: uppercase; }
  .offer__headline { font-weight: 700; font-size: 34px; line-height: 44px; }
  .offer__deal { font-weight: 600; font-size: 27px; line-height: 40px; }
  .offer__note { font-weight: 300; font-size: 22px; line-height: 40px; }

  .shipping { position: absolute; top: 378px; left: 380px; display: flex; gap: 34px; list-style: none; }
  .shipping__item {
    display: flex; gap: 14px; color: var(--text-light);
    font-family: "Oswald", sans-serif; font-weight: 600; font-size: 23px; line-height: 30px; text-transform: uppercase;
  }
  .shipping__bullet { width: 16px; height: 16px; margin-top: 6px; background: var(--rare-pink-deep); flex: none; }
</style>
</head>
<body>
<main class="canvas">

  <section class="banner banner--wild" aria-label="B Wild banner">
    <svg class="banner__backdrop" width="1000" height="563" viewBox="0 0 1000 563" aria-hidden="true">
      <defs>
        <linearGradient id="wild-sky" x1="0" y1="0" x2="1" y2="1">
          <stop offset="0" stop-color="#d8ecff"/>
          <stop offset="0.35" stop-color="#2f7fd0"/>
          <stop offset="0.75" stop-color="#0d2c5c"/>
          <stop offset="1" stop-color="#07101e"/>
        </linearGradient>
        <radialGradient id="wild-glow" cx="0.72" cy="0.42" r="0.5">
          <stop offset="0" stop-color="#3aa8ff" stop-opacity="0.35"/>
          <stop offset="1" stop-color="#3aa8ff" stop-opacity="0"/>
        </radialGradient>
      </defs>
      <rect width="1000" height="563" fill="#0b0d12"/>
      <polygon points="0,0 860,0 560,563 0,563" fill="url(#wild-sky)" role="img" aria-label="Stormy blue sky over cracked earth"/>
      <polygon points="440,0 520,0 120,563 40,563" fill="var(--stripe-grey)"/>
      <polygon points="700,0 820,0 400,563 280,563" fill="rgba(10,40,90,0.45)"/>
      <rect width="1000" height="563" fill="url(#wild-glow)"/>
      <line x1="0" y1="73" x2="1000" y2="73" stroke="var(--frame-line)" stroke-width="1.5"/>
      <line x1="0" y1="483" x2="1000" y2="483" stroke="var(--frame-line)" stroke-width="1.5"/>
      <line x1="958" y1="40" x2="958" y2="526" stroke="var(--frame-line)" stroke-width="1.5"/>
      <rect y="526" width="1000" height="37" fill="var(--wild-band)"/>
    </svg>

    <div class="photo photo--models" role="img" aria-label="Two athletes wearing patterned arm sleeves, one seated on a weight bench holding a plate"></div>

    <div class="brand"><span class="brand__mark"></span><span class="brand__name">Velto-Primed Sports</span></div>

    <h2 class="slogan">B WILD</h2>

    <div class="offer">
      <p class="offer__headline">Mix-n-Match</p>
      <p class="offer__deal">5 for $50, &amp; Free Shipping</p>
      <p class="offer__note">(Any sleeve or headband)</p>
    </div>
  </section>

  <section class="banner banner--rare" aria-label="B Rare banner">
    <svg class="banner__backdrop" width="1000" height="563" viewBox="0 0 1000 563" aria-hidden="true">
      <defs>
        <linearGradient id="rare-wash" x1="0" y1="0" x2="1" y2="1">
          <stop offset="0" stop-color="#5a1028"/>
          <stop offset="0.5" stop-color="#8c1a44"/>
          <stop offset="1" stop-color="#2a0a16"/>
        </linearGradient>
        <linearGradient id="rare-city" x1="0" y1="0" x2="0" y2="1">
          <stop offset="0" stop-color="#6a6d74" stop-opacity="0.6"/>
          <stop offset="1" stop-color="#1a1b1f" stop-opacity="0.9"/>
        </linearGradient>
        <radialGradient id="rare-glow" cx="0.75" cy="0.4" r="0.45">
          <stop offset="0" stop-color="#ff4fb0" stop-opacity="0.35"/>
          <stop offset="1" stop-color="#ff4fb0" stop-opacity="0"/>
        </radialGradient>
      </defs>
      <rect width="1000" height="563" fill="#121215"/>
      <polygon points="0,0 600,0 200,563 0,563" fill="url(#rare-wash)"/>
      <polygon points="600,0 760,0 360,563 200,563" fill="var(--stripe-grey)"/>
      <rect x="280" y="260" width="720" height="266" fill="url(#rare-city)" role="img" aria-label="Faded city skyline"/>
      <rect width="1000" height="563" fill="url(#rare-glow)"/>
      <line x1="0" y1="73" x2="1000" y2="73" stroke="var(--frame-line)" stroke-width="1.5"/>
      <line x1="0" y1="483" x2="1000" y2="483" stroke="var(--frame-line)" stroke-width="1.5"/>
      <line x1="958" y1="40" x2="958" y2="526" stroke="var(--frame-line)" stroke-width="1.5"/>
      <rect y="522" width="1000" height="41" fill="var(--rare-band)"/>
    </svg>

    <div class="photo photo--model" role="img" aria-label="Athlete with curly blonde hair wearing a pink camo headband, looking down"></div>

    <div class="brand"><span class="brand__mark"></span><span class="brand__name">Velto-Primed Sports</span></div>

    <h2 class="slogan">B RARE</h2>

    <ul class="shipping">
      <li class="shipping__item"><span class="shipping__bullet"></span><span>Free U.S. shipping on<br>orders over $50</span></li>
      <li class="shipping__item"><span class="shipping__bullet"></span><span>$3.99 shipping on<br>everything else</span></li>
    </ul>
  </section>

</main>
</body>
</html>
```